We are a small NZ based company looking to rebrand our eco chem free cleaning product Purova

This product was launched in 2021. The brand and labeling were aimed at the consumer who cared that the cleaning products they bought into their home were not only effective but non-harmful to their families and the environment. The label was a little bohemian/ natural. We feel that the labels now need to be more chic and classy, They need to look stylish in a country cottage as well as a high end minimalist home. Colours need to be mute so as to fit with most decors.
We need help with font colour and type - layout and balance. Trigger/ pump colour.
I have attached photos of our current range and labels
A couple of mock ups we are working on - (struggling with )
A colour pallet
The two last PNG files are closer to where we want to end up but they are not really right.

The products are sold online only
Our website is www.purova.co.nz
The Brand board that we had done sometime ago is that last file.
Most of the colours on the labels are ok - except the apricot on the foaming hand soap bottle and the colour on the all purpose bottle - neither of which we love.
The Fair Tide bottles are closer to what we are thinking.
Canva Links
https://www.sketchloft.example/design/QWRTplmzx41/hbnKyeTgrQuvs93LdwPoZa/edit
https://www.sketchloft.example/design/QWRTvbn7UoXc/kPmWq2RzTyhNb4VfGsLeXd/edit
https://www.sketchloft.example/design/QWRTzh3KLaNp/yt6BemRwPoiLx81CvdNqTe/edit
https://www.sketchloft.example/design/QWRTfk8MsaTq/Lu5DrpXwgYoBj72MnhKzsc/edit

Target Market(s)

Mothers who care about the products they bring into there homes but also want the product to look good in the home

Industry/Entity Type

Cleaning products

Requirements
Must have
• Design must be chic - and be able to sit and look great in any modern bathroom or kitchen.

```html
<!DOCTYPE html>
<html lang="en">
<head>
<meta charset="utf-8">
<title>Purova Cleaner Range Labels</title>
<link href="https://fonts.googleapis.com/css2?family=Questrial&family=Montserrat:wght@600&display=swap" rel="stylesheet">
<style>
  :root {
    --backdrop: #d2d2d2;
    --label: #ffffff;
    --brand-green: #6f9580;
    --text-sage: #7d9c8c;
    --flower-light: #fbfbf8;
    --flower-tint: #e9eeeb;
    --bathroom: #e2a623;
    --glass: #57a7b3;
    --all-purpose: #a98787;
  }
  * { margin: 0; padding: 0; box-sizing: border-box; }
  html, body {
    width: 1200px;
    height: 801px;
    overflow: hidden;
    background: var(--backdrop);
  }
  .range {
    position: relative;
    width: 1200px;
    height: 801px;
  }
  .label {
    position: absolute;
    top: 180px;
    width: 300px;
    height: 440px;
    margin-left: -150px;
    background: var(--label);
    border-radius: 8px;
    text-align: center;
    font-family: "Questrial", sans-serif;
    color: var(--text-sage);
  }
  .label--bathroom { left: 258px; }
  .label--glass { left: 601px; }
  .label--all-purpose { left: 943px; }

  .brand {
    position: absolute;
    top: 32px;
    left: 0;
    right: 0;
    height: 36px;
    display: flex;
    align-items: center;
    justify-content: center;
    gap: 10px;
  }
  .brand__dot {
    width: 22px;
    height: 22px;
    border-radius: 50%;
    background: var(--brand-green);
  }
  .brand__name {
    font-size: 36px;
    line-height: 1;
    color: var(--brand-green);
  }
  .brand__rule {
    position: absolute;
    top: 74px;
    left: 52px;
    right: 52px;
    height: 1px;
    background: var(--brand-green);
  }
  .tagline {
    position: absolute;
    top: 80px;
    left: 0;
    right: 0;
    font-size: 13.5px;
    line-height: 16px;
    color: var(--brand-green);
  }
  .flower {
    position: absolute;
    top: 119px;
    left: 50%;
    width: 167px;
    height: 167px;
    margin-left: -83.5px;
    border-radius: 50%;
    background: radial-gradient(circle at 50% 45%, var(--flower-light) 0 40%, var(--flower-tint) 75%);
  }
  .product {
    position: absolute;
    top: 261px;
    left: 0;
    right: 0;
    font-family: "Montserrat", sans-serif;
    font-weight: 600;
    font-size: 29px;
    letter-spacing: 2px;
    line-height: 30px;
    white-space: nowrap;
  }
  .product--bathroom { color: var(--bathroom); }
  .product--glass { color: var(--glass); }
  .product--all-purpose { color: var(--all-purpose); }
  .product-type {
    position: absolute;
    top: 296px;
    left: 0;
    right: 0;
    font-size: 19px;
    line-height: 22px;
    letter-spacing: 1px;
  }
  .uses {
    position: absolute;
    top: 344px;
    left: 0;
    right: 0;
    font-size: 12.5px;
    line-height: 14px;
  }
  .volume {
    position: absolute;
    top: 398px;
    left: 0;
    right: 0;
    font-size: 11px;
    line-height: 14px;
  }
</style>
</head>
<body>
<main class="range">

  <section class="label label--bathroom">
    <div class="brand"><span class="brand__dot"></span><span class="brand__name">Purova</span></div>
    <div class="brand__rule"></div>
    <p class="tagline">The Power Of Chamomile</p>
    <div class="flower" role="img" aria-label="Photograph of a white chamomile flower"></div>
    <h2 class="product product--bathroom">BATHROOM</h2>
    <p class="product-type">CLEANER</p>
    <p class="uses">Shower | Bath | Toilet<br>Tiles &amp; Grout</p>
    <p class="volume">500ml</p>
  </section>

  <section class="label label--glass">
    <div class="brand"><span class="brand__dot"></span><span class="brand__name">Purova</span></div>
    <div class="brand__rule"></div>
    <p class="tagline">The Power Of Chamomile</p>
    <div class="flower" role="img" aria-label="Photograph of a white chamomile flower"></div>
    <h2 class="product product--glass">GLASS</h2>
    <p class="product-type">CLEANER</p>
    <p class="uses">Windows | Glass | Stainless Steel<br>Reflective Surfaces</p>
    <p class="volume">500ml</p>
  </section>

  <section class="label label--all-purpose">
    <div class="brand"><span class="brand__dot"></span><span class="brand__name">Purova</span></div>
    <div class="brand__rule"></div>
    <p class="tagline">The Power Of Chamomile</p>
    <div class="flower" role="img" aria-label="Photograph of a white chamomile flower"></div>
    <h2 class="product product--all-purpose">ALL PURPOSE</h2>
    <p class="product-type">CLEANER</p>
    <p class="uses">Surfaces | Stains<br>Grease &amp; Grime</p>
    <p class="volume">500ml</p>
  </section>

</main>
</body>
</html>
```